New Letterhead request for our Law Firm!

We are a small Estate Planning Firm who just got out logo redesigned. It's attached. We need some letterhead for our client welcome letters and so forth. Clean, bright, and approachable is our style. If you need the specifications for our color scheme or other versions of the logo file, we have those too. Visit our website to get an idea about our services/aesthetics:https://bramblecove.law/

Target Market(s)

Adults 30-80

Colors

Designer to choose colors to be used in the design.

Requirements
Must have
• Logo with color. Contact information

```html
<!DOCTYPE html>
<html lang="en">
<head>
<meta charset="utf-8">
<title>Bramble Cove Law Firm – Letterhead</title>
<link rel="stylesheet" href="https://fonts.googleapis.com/css2?family=Roboto+Slab:wght@400;600&family=Montserrat:wght@300;400;600&display=swap">
<style>
  :root {
    --green: #6fa889;
    --green-soft: #a9ccb8;
    --ink: #2d2d2d;
    --grey: #8a8a8a;
    --grey-light: #c9c9c9;
    --paper: #ffffff;
    --backdrop: #eef0f2;
  }
  html, body {
    margin: 0; padding: 0;
    width: 1200px; height: 1200px;
    overflow: hidden;
    background: var(--backdrop);
  }
  .letterhead {
    position: absolute;
    left: 190px; top: 70px;
    width: 820px; height: 1061px;
    background: var(--paper);
    box-shadow: 0 6px 24px rgba(0,0,0,.08);
    font-family: "Montserrat", sans-serif;
    color: var(--ink);
  }
  .brand {
    position: absolute; left: 60px; top: 58px;
    display: flex; align-items: center; gap: 14px;
  }
  .brand-mark {
    width: 58px; height: 58px; border-radius: 50%;
    border: 2px solid var(--green);
  }
  .brand-name {
    font-family: "Roboto Slab", serif; font-weight: 600;
    color: var(--green); line-height: 1.05;
    letter-spacing: 2px;
  }
  .brand-name .primary { font-size: 25px; display: block; }
  .brand-name .secondary { font-size: 13px; display: block; letter-spacing: 4px; }
  .firm-contact {
    position: absolute; right: 60px; top: 62px; text-align: right;
  }
  .firm-legal {
    font-family: "Roboto Slab", serif; font-weight: 600;
    font-size: 10px; letter-spacing: 1px; text-transform: uppercase;
  }
  .firm-phone {
    display: flex; align-items: center; justify-content: flex-end; gap: 8px;
    margin-top: 6px; font-size: 21px; font-weight: 300; color: var(--grey-light);
  }
  .firm-phone svg { width: 20px; height: 20px; }
  .letter-date {
    position: absolute; right: 60px; top: 150px;
    font-size: 10px; color: var(--ink);
  }
  .letter-date span { color: var(--green); }
  .recipient { position: absolute; left: 100px; top: 200px; }
  .recipient-name {
    font-family: "Roboto Slab", serif; font-weight: 600;
    color: var(--green); font-size: 16px;
  }
  .recipient-role {
    font-size: 8px; font-weight: 600; letter-spacing: 1px; text-transform: uppercase;
    margin-top: 3px;
  }
  .letter-body {
    position: absolute; left: 100px; right: 100px; top: 270px;
    font-size: 12px; line-height: 1.85; color: var(--grey);
  }
  .letter-body p { margin: 0 0 22px; }
  .sign-off { position: absolute; left: 100px; top: 640px; }
  .signature {
    width: 220px; height: 70px; border-radius: 4px;
    background: linear-gradient(90deg, #f3f3f3, #e6e6e6);
  }
  .signer-name {
    font-family: "Roboto Slab", serif; font-weight: 600;
    color: var(--green); font-size: 15px; margin-top: 10px;
  }
  .signer-role {
    font-size: 8px; font-weight: 600; letter-spacing: 1px; margin-top: 3px;
  }
  .footer { position: absolute; left: 60px; right: 60px; bottom: 70px; }
  .footer-rule {
    display: flex; align-items: center; gap: 14px;
  }
  .footer-rule .line { flex: 1; height: 2px; background: var(--green-soft); }
  .footer-icon { width: 22px; height: 22px; }
  .footer-text {
    text-align: center; margin-top: 14px;
    font-family: "Roboto Slab", serif; font-weight: 600;
    font-size: 12px; letter-spacing: .5px;
  }
  .footer-text.small {
    margin-top: 5px; font-family: "Montserrat", sans-serif; font-weight: 400; font-size: 10px;
  }
</style>
</head>
<body>
<main class="letterhead">
  <header>
    <div class="brand">
      <div class="brand-mark"></div>
      <div class="brand-name">
        <span class="primary">BRAMBLE COVE</span>
        <span class="secondary">LAW FIRM</span>
      </div>
    </div>
    <div class="firm-contact">
      <div class="firm-legal">Bramble Cove Law Firm, PLLC</div>
      <div class="firm-phone">
        <svg viewBox="0 0 20 20"><circle cx="10" cy="10" r="10" fill="#6fa889"/><path d="M7 5.5l1.6 2.2-1 1.2c.6 1.3 1.5 2.2 2.8 2.8l1.2-1 2.2 1.6-.8 1.8c-3.8-.3-6.6-3.1-6.9-6.9z" fill="#fff"/></svg>
        612 555 0187
      </div>
    </div>
  </header>

  <div class="letter-date"><span>Date:</span> 15-11-2019</div>

  <section class="recipient">
    <div class="recipient-name">Dana Whitfield</div>
    <div class="recipient-role">CEO, Harbor Lane Co.</div>
  </section>

  <section class="letter-body">
    <p>Thank you for choosing our firm to guide your estate planning. We are glad to welcome you and your family, and we look forward to helping you protect what matters most. This letter outlines the next steps, the documents we will prepare together, and what you can expect during our first meetings.</p>
    <p>Before our next visit, please gather recent account statements, property deeds, insurance policies and any existing wills or trusts. A short checklist is enclosed to help you stay organized.</p>
    <p>If you have questions at any time, simply call or email our office. We are here to make the process clear and comfortable.</p>
  </section>

  <section class="sign-off">
    <div class="signature" role="img" aria-label="Handwritten signature of Martin Alcott"></div>
    <div class="signer-name">Martin Alcott</div>
    <div class="signer-role">ATTORNEY/LAWYER</div>
  </section>

  <footer class="footer">
    <div class="footer-rule">
      <div class="line"></div>
      <svg class="footer-icon" viewBox="0 0 22 22"><circle cx="11" cy="11" r="11" fill="#6fa889"/><path d="M11 5a3.6 3.6 0 0 0-3.6 3.6c0 2.7 3.6 7 3.6 7s3.6-4.3 3.6-7A3.6 3.6 0 0 0 11 5zm0 5a1.4 1.4 0 1 1 0-2.8 1.4 1.4 0 0 1 0 2.8z" fill="#fff"/></svg>
      <svg class="footer-icon" viewBox="0 0 22 22"><circle cx="11" cy="11" r="11" fill="#6fa889"/><path d="M7.5 6l1.7 2.4-1 1.3c.6 1.4 1.6 2.4 3 3l1.3-1 2.4 1.7-.9 1.9C10 15 7 12 6.6 7.8z" fill="#fff"/></svg>
      <svg class="footer-icon" viewBox="0 0 22 22"><circle cx="11" cy="11" r="11" fill="#6fa889"/><rect x="6" y="7.5" width="10" height="7" rx="1" fill="#fff"/><path d="M6.3 8l4.7 3.5L15.7 8" fill="none" stroke="#6fa889" stroke-width="1"/></svg>
      <svg class="footer-icon" viewBox="0 0 22 22"><circle cx="11" cy="11" r="11" fill="#6fa889"/><circle cx="11" cy="11" r="5" fill="none" stroke="#fff" stroke-width="1.2"/><path d="M6 11h10M11 6c-2.2 2.8-2.2 7.2 0 10M11 6c2.2 2.8 2.2 7.2 0 10" fill="none" stroke="#fff" stroke-width="1"/></svg>
      <div class="line"></div>
    </div>
    <div class="footer-text">2400 Larch Avenue, Suite 310 &nbsp;|&nbsp; Fairview, MN 55099</div>
    <div class="footer-text small">612 555 0187 &nbsp;|&nbsp; info@bramblecove.law &nbsp;|&nbsp; www.bramblecove.law</div>
  </footer>
</main>
</body>
</html>
```